"Maple Hollow" red wine label design

We are a Sydney based company. We need to design a wine label for a Australian red wine.
Front label include following info:
Our brand: "Maple Hollow";
Product name: "Shiraz 2016";
In the bottom with small font: "Wine of Australia", "750ml"
Back label:
the back label would need to be consistent with the front label, with space for one paragraph of tasting notes, and ingredient info etc.
we would like to use white, gold and blue in this label. It should make customer feel the magical and beautiful moment of starry night.

We also need a logo design for the wine brand: "Maple Hollow"

I have attached a few wine bottle that used blue to give you some inspirations.

We need the design in AI file format.

Target Market(s)

both men and women

Industry/Entity Type

It Company

Logo Text

Maple Hollow

Requirements
Nice to have
• gold borderline, words; use of blue and white

```html
<!DOCTYPE html>
<html lang="en">
<head>
<meta charset="utf-8">
<title>Maple Hollow Shiraz 2016 – Front Label</title>
<link href="https://fonts.googleapis.com/css2?family=Alex+Brush&family=Montserrat:wght@400;600&display=swap" rel="stylesheet">
<style>
  :root {
    --page-bg: #f2f2f2;
    --night-navy: #0c1829;
    --deep-blue: #16304a;
    --ridge-blue: #2e5a70;
    --mist-blue: #8fb4c2;
    --frost: #e4f2ef;
    --gold: #a8894f;
    --gold-text: #8a6f3c;
    --ink-muted: #7b8583;
  }
  * { margin: 0; padding: 0; box-sizing: border-box; }
  html, body {
    width: 1200px;
    height: 1020px;
    overflow: hidden;
    background: var(--page-bg);
  }
  .canvas {
    position: relative;
    width: 1200px;
    height: 1020px;
  }
  .label {
    position: absolute;
    left: 365px;
    top: 40px;
    width: 470px;
    height: 940px;
    background: var(--frost);
    overflow: hidden;
  }
  .label__artwork {
    position: absolute;
    inset: 0 0 220px 0;
    background: linear-gradient(
      to bottom,
      var(--night-navy) 0%,
      var(--deep-blue) 48%,
      var(--ridge-blue) 70%,
      var(--mist-blue) 90%,
      var(--frost) 100%
    );
  }
  .label__frame {
    position: absolute;
    inset: 16px;
    border: 1.5px solid var(--gold);
  }
  .label__brand {
    position: absolute;
    left: 48px;
    top: 200px;
    font-family: "Alex Brush", cursive;
    font-weight: 400;
    color: var(--gold);
    font-size: 96px;
    line-height: 0.9;
  }
  .label__brand-line { display: block; }
  .label__brand-line--second { padding-left: 120px; }
  .label__details {
    position: absolute;
    left: 0;
    right: 0;
    top: 790px;
    text-align: center;
    font-family: "Montserrat", sans-serif;
  }
  .label__product {
    font-weight: 600;
    font-size: 22px;
    letter-spacing: 0.5px;
    color: var(--gold-text);
    margin-bottom: 26px;
  }
  .label__meta {
    font-weight: 400;
    font-size: 13px;
    line-height: 24px;
    color: var(--ink-muted);
  }
</style>
</head>
<body>
  <main class="canvas">
    <section class="label">
      <div class="label__artwork" role="img" aria-label="Night sky scattered with small stars above layered blue mountain ridges fading into pale mist"></div>
      <div class="label__frame"></div>
      <h1 class="label__brand">
        <span class="label__brand-line">Maple</span>
        <span class="label__brand-line label__brand-line--second">Hollow</span>
      </h1>
      <div class="label__details">
        <p class="label__product">Shiraz 2016</p>
        <p class="label__meta">700ml</p>
        <p class="label__meta">Wine of Australia</p>
      </div>
    </section>
  </main>
</body>
</html>
```